Web Design Project: Facility Management company

Hi! We need a new website.

Our current website: http://www.vireo-trade.ru/ and we don-t like it. =)
The structure of our company has changed and now we don't need "cleaning" and "engeneering" on this site.

We are facility management company in Russia. So we provide integrated service solutions specific to industrial services: maintenance, repair, etc. of engineering systems.
More services:
Energy planning
Automation
Audit
Statements with regulators
Video surveillance
Central heating
Security systems
Welding
Management of subcontractors
Electrical installation and service needs
Reception
Catering

Visitors:
* Managers in the field of commercial real estate
* Chief engineers
* TOP managers of large companies, malls, factories...
+ their subordinates
* Small% of applicants.

Here you can see some websites/patterns we liked:
http://www.kobalmire.ru/ (This is our competitor’s site, so our site shouldn’t be an exact copy))))
http://www.dwatqo.ru/
http://www.layoutfarrow.com/demo/24296.html
http://www.layoutfarrow.com/website-templates/10145.html

Style:
Light, hi-tech/minimalizm, the color palette should be based on the original site colors (Green + black + white). http://www.vireo-trade.ru/

Estimated sitemap:
1. Home
2. About Us
3. Company's policy
4. History + Achievements.
5. Certificates
6. Map of presence (Here you can use sample map in file "our projects")
7. Services
8. Portfolio
9. News or blog
10. Jobs
11. Contacts - with the feedback form (or the function "call to order")
12. English

Need a design pages: main page, page 404. The rest of the page could be created by general pattern.

Logo, navigation bar and contacts should be visible on all pages of a site.
Flash animation elements and buttons, etc. - not needed.

* We need to develop 3 websites, so we are looking for a long term cooperation.
Looking forward to your creativity =)

Must Have:
Clear, intuitive structure of web pages.
In the center - of pictures reflecting our main services (industrial theme). May be in rotation.
BUT! This banner (central picture) should not be a huge one =)
All relevant information should be visible at once without scrolling.

A possibility to place media files (presentations, video ...) and 2 banner links on the main page.

Font should be available in Cyrillic.
Updates

IMPORTANT!

Please notice that in thisdesign we don't need "cleaning" and "engeneering" on this site.

So don't use old block of 4pictures from our current website. We don't need it anymore. 

Thestructure of our company has changed and now we need some links (may be banners,may be something else) to our future cleaning website as well as engeneeringwebsite.
It should look like seperate (partner) companies, not like our sevices.

Regards, Vera.

Please don't forget that we need bilingual site.

So define language changing tool in your designs.

Industry/Entity Type

Industrial

```html
<!DOCTYPE html>
<html lang="en">
<head>
<meta charset="utf-8">
<title>Vireo Trade — Home</title>
<link rel="stylesheet" href="https://fonts.googleapis.com/css2?family=Arimo:wght@400;700&display=swap">
<style>
:root{
  --page-bg:#5f8b1f;
  --panel:#ffffff;
  --green:#6f9a26;
  --green-btn:#8cb145;
  --green-menu:rgba(134,174,62,.93);
  --ink:#222;
  --muted:#777;
  --grey-box:#e4e4e4;
  --rule:#dcdcdc;
}
*{margin:0;padding:0;box-sizing:border-box}
html,body{width:1200px;height:960px;overflow:hidden}
body{background:var(--page-bg);font-family:"Arimo",Arial,sans-serif;color:var(--ink);position:relative}
a{color:inherit;text-decoration:none}
.abs{position:absolute}

.top-links{font-size:11px;color:#a9c87a;top:20px}
.top-links a{margin-right:22px}
.top-links .current{color:#fff;text-decoration:underline}
.lang{left:223px}
.util{left:845px}

.page{left:192px;top:40px;width:816px;height:794px;background:var(--panel);box-shadow:0 0 14px rgba(0,0,0,.35);overflow:hidden}
.header-band{left:0;top:90px;width:816px;height:70px;background:linear-gradient(#fff,#ececec 60%,#f6f6f6)}
.lower-band{left:0;top:320px;width:816px;height:474px;background:linear-gradient(#ededed,#fafafa 30%,#fff 70%,#efefef)}

.brand{left:31px;top:34px;display:flex;align-items:center;gap:10px;font-size:26px;letter-spacing:4px;color:#1d1d1d}
.brand-mark{width:18px;height:18px;background:var(--green-btn)}

.main-nav{left:341px;top:52px;display:flex;font-size:12px;color:#555}
.main-nav a{position:absolute;white-space:nowrap}
.main-nav .active{color:var(--green)}
.main-nav .open{color:#222}
.nav-rule{left:336px;top:71px;width:448px;height:3px;background:#e2e2e2}
.nav-rule-home{left:336px;top:71px;width:50px;height:3px;background:var(--green-btn)}
.nav-rule-services{left:672px;top:71px;width:54px;height:3px;background:var(--green-btn)}

.slider{left:33px;top:121px;width:493px;height:180px;border-radius:3px;background:linear-gradient(160deg,#4a5563,#8f9db0 45%,#c9cfdb 75%,#d6cfd4)}
.slider-prev{left:30px;top:70px}
.slider-dots{left:225px;top:165px;display:flex;gap:5px}
.slider-dots i{width:4px;height:4px;border-radius:50%;background:#ddd}
.slider-dots i:first-child{background:#fff}

.field{background:var(--grey-box);border-radius:4px}
.field-1{left:561px;top:146px;width:222px;height:32px}
.field-2{left:561px;top:185px;width:222px;height:72px}
.btn{background:var(--green-btn);color:#fff;font-size:10.5px;font-weight:700;border-radius:3px;display:flex;align-items:center;justify-content:center;gap:6px}
.btn-send{left:722px;top:228px;width:54px;height:23px}
.call{left:576px;top:276px;font-size:14px;color:var(--green)}
.call strong{font-size:17px}

.dropdown{left:436px;top:83px;width:280px;height:166px;background:var(--green-menu);border-radius:3px;font-size:11.5px;color:#fff}
.dropdown a{position:absolute}
.dropdown .current{color:#1d1d1d;text-decoration:underline}

.section-title{font-size:15px;color:var(--green)}
.section-rule{height:1px;background:var(--rule)}
.about-title{left:55px;top:347px}
.about-rule{left:33px;top:369px;width:495px}
.about-text{left:55px;top:388px;width:206px;font-size:9.6px;line-height:14.4px;color:var(--muted)}
.about-text em{color:var(--green);font-weight:700;text-decoration:underline}

.video{left:295px;top:388px;width:217px;height:127px;border-radius:4px;background:linear-gradient(#3b4650,#6b7a88 50%,#2f3840)}
.video-bar{left:0;top:0;width:217px;height:30px;background:rgba(40,40,40,.55);border-radius:4px 4px 0 0;color:#ddd;font-size:11px;text-align:center;line-height:30px}
.video-play{left:81px;top:50px}

.side-box{background:#e6e6e6;border-radius:4px}
.services-box{left:560px;top:333px;width:223px;height:178px}
.box-title{left:14px;top:11px;font-size:13px;color:var(--green)}
.box-rule{left:10px;top:34px;width:203px;height:1px;background:#d3d3d3}
.service-list{left:14px;top:51px;font-size:11px;color:#666;line-height:24px}
.service-list .current{color:var(--green);font-weight:700;text-decoration:underline}
.btn-more{left:113px;top:147px;width:103px;height:24px}

.news-title{left:55px;top:553px;font-size:12px;font-weight:700;color:var(--green)}
.news-rule{left:33px;top:579px;width:495px}
.news-img{width:215px;height:64px;border-radius:4px;background:linear-gradient(90deg,#203a66,#5d86c0 45%,#8fb6e0)}
.news-img-1{left:48px;top:599px}
.news-img-2{left:295px;top:599px;background:linear-gradient(90deg,#2d4c7d,#6e97c8 50%,#c0d4e8)}
.news-item{width:215px;font-size:9.6px;line-height:14.2px;color:var(--muted)}
.news-item h3{font-size:11px;color:var(--green);line-height:14px}
.news-item .date{color:#333;font-weight:700}
.news-1{left:55px;top:682px}
.news-2{left:302px;top:682px}

.projects-box{left:560px;top:543px;width:223px;height:227px}
.map{left:7px;top:46px;width:208px;height:167px;background:linear-gradient(135deg,#fff 10%,#9be05e 35%,#8ed451 70%,#fff 95%)}

.footer{left:247px;top:857px;font-size:11px;color:#1d2a0a;line-height:17px}
.footer .current{color:#fff;text-decoration:underline}
.copyright{left:835px;top:857px;font-size:11px;color:#1d2a0a}
.copyright b{color:#fff;font-weight:400}
</style>
</head>
<body>

<nav class="abs top-links lang"><a class="current" href="#">English</a><a href="#">Russian</a></nav>
<nav class="abs top-links util"><a href="#">News</a><a class="current" href="#">Jobs</a><a href="#">Contact</a></nav>

<div class="abs page">
  <div class="abs header-band"></div>
  <div class="abs lower-band"></div>

  <a class="abs brand" href="#"><span class="brand-mark"></span>VIREO TRADE</a>

  <div class="abs nav-rule"></div>
  <div class="abs nav-rule-home"></div>
  <div class="abs nav-rule-services"></div>
  <nav class="abs main-nav">
    <a class="active" style="left:0">Home</a>
    <a style="left:53px">About Us</a>
    <a style="left:121px">History &amp; Achievements</a>
    <a style="left:257px">Certificates</a>
    <a class="open" style="left:333px">Services</a>
    <a style="left:396px">Portfolio</a>
  </nav>

  <div class="abs slider" role="img" aria-label="Rotating banner: glass office towers seen from below">
    <svg class="abs slider-prev" width="34" height="34" viewBox="0 0 34 34"><circle cx="17" cy="17" r="15" fill="none" stroke="#ddd" stroke-width="3" opacity=".8"/><path d="M20 10l-7 7 7 7" fill="none" stroke="#ddd" stroke-width="3"/></svg>
    <div class="abs slider-dots"><i></i><i></i><i></i><i></i><i></i></div>
  </div>

  <div class="abs field field-1"></div>
  <div class="abs field field-2"></div>
  <a class="abs btn btn-send" href="#">Send</a>
  <p class="abs call">Or call us at <strong>+7 812 555 0148</strong></p>

  <div class="abs dropdown">
    <a style="left:16px;top:12px">Service 1</a>
    <a style="left:16px;top:36px">Service 2</a>
    <a style="left:16px;top:60px">Service 3</a>
    <a style="left:16px;top:84px">Service 4</a>
    <a style="left:16px;top:108px">Service 5</a>
    <a style="left:16px;top:132px">Service 6</a>
    <a style="left:152px;top:12px">Service 7</a>
    <a style="left:152px;top:36px">Service 8</a>
    <a class="current" style="left:152px;top:60px">Service 9</a>
    <a style="left:152px;top:84px">Service 10</a>
    <a style="left:152px;top:108px">Service 11</a>
    <a style="left:152px;top:132px">Service 12</a>
  </div>

  <h2 class="abs section-title about-title">About Us</h2>
  <div class="abs section-rule about-rule"></div>
  <p class="abs about-text">We work next to you already for more than 8 years. Once we became one of the first companies, which decided to develop an integrated facility management of real estate in Russia. Today more than 500 professionals are <em>employed with us</em>, there are dozens of projects in the business portfolio: from small bank branch to super-regional shopping centre.</p>

  <div class="abs video" role="img" aria-label="Presentation video still: office towers">
    <div class="abs video-bar">Our presentation video</div>
    <svg class="abs video-play" width="46" height="46" viewBox="0 0 46 46"><circle cx="23" cy="23" r="22" fill="rgba(255,255,255,.35)"/><path d="M19 14l9 9-9 9" fill="none" stroke="#fff" stroke-width="4"/></svg>
  </div>

  <aside class="abs side-box services-box">
    <h2 class="abs box-title">Services</h2>
    <div class="abs box-rule"></div>
    <ul class="abs service-list" style="list-style:none">
      <li class="current">Service 1</li><li>Service 2</li><li>Service 3</li><li>Service 4</li>
    </ul>
    <a class="abs btn btn-more" href="#">More services
      <svg width="9" height="9" viewBox="0 0 9 9"><path d="M1 1l3.5 3 3.5-3M1 5l3.5 3 3.5-3" fill="none" stroke="#fff" stroke-width="1.4"/></svg></a>
  </aside>

  <h2 class="abs news-title">Latest news</h2>
  <div class="abs section-rule news-rule"></div>
  <div class="abs news-img news-img-1" role="img" aria-label="News photo: office buildings against blue sky"></div>
  <div class="abs news-img news-img-2" role="img" aria-label="News photo: towers and street lamp"></div>
  <article class="abs news-item news-1">
    <h3>Lorem ipsum dolor sit amet</h3>
    <p class="date">[ 11.9.2012 ]</p>
    <p>Consectetur adipiscing elit. Sed est ante, sagittis sit amet sollicitudin at, sagittis ut lacus. Nullam at risus est, ut pretium ligula.</p>
  </article>
  <article class="abs news-item news-2">
    <h3>Morbi tincidunt, arcu eget aliquam adipiscing</h3>
    <p class="date">[ 29.7.2012 ]</p>
    <p>Sed nibh diam, accumsan quis egestas vitae, iaculis vel erat. Vestibulum nunc est, feugiat eu mollis sed, blandit id mi.</p>
  </article>

  <aside class="abs side-box projects-box">
    <h2 class="abs box-title">Our projects</h2>
    <div class="abs box-rule"></div>
    <div class="abs map" role="img" aria-label="Map of regions with project locations marked"></div>
  </aside>
</div>

<footer>
  <p class="abs footer">Company &nbsp;|&nbsp; Chosen by &nbsp;|&nbsp; Our team &nbsp;|&nbsp; <a class="current" href="#">Contact us</a> &nbsp;|&nbsp; Integrated facility management<br>Technical maintenance of engineering systems &nbsp;|&nbsp; Professional cleaning &nbsp;|&nbsp; Civil engineering</p>
  <p class="abs copyright">Copyright © 2012 <b>Vireo Trade</b></p>
</footer>

</body>
</html>
```